BRISKWAY traffic management plans

The preparation of traffic management plans for architects, builders, landscapers for council approval. The preparation of the plans can include submitting to council, briefing the builder regarding management of the plan, onsite visit, taking photographs, measurements and establishing the best outcome. Implementing the plan can also take place if need be.
NO EXISTING LOGO AVAILABLE
No photos or documents available to upload

Target Market(s)

Builders, architects, landscapers
No existing logo availalble

Industry/Entity Type

Builders

Contact Information for Business Card

BRISKWAY Traffic Management Plans
Tom Brindley
harbourlane@zentrynet.com.au
0427 693 058

Font styles to use
Serif

Colors
1b1b1b

Requirements
Must have
• competitive prices
• No existing logo available
• No photos available
Nice to have
• Black with orange and white
• No existing logo available no
Should not have
• no existing logo available
• No photos or documents to upload

```html
<!DOCTYPE html>
<html lang="en">
<head>
<meta charset="utf-8">
<title>Briskway Traffic Management Plans – Business Card</title>
<link rel="stylesheet" href="https://fonts.googleapis.com/css2?family=Open+Sans:wght@400;600;700&display=swap">
<style>
  :root {
    --ink: #1b1b1b;
    --black: #000000;
    --paper: #ffffff;
    --paper-shade: #ececec;
    --backdrop: #d9d6d1;
    --card-w: 520px;
    --card-h: 318px;
  }
  * { box-sizing: border-box; margin: 0; padding: 0; }
  html, body {
    width: 1200px;
    height: 900px;
    overflow: hidden;
    background: var(--backdrop);
  }
  .sheet {
    width: 1200px;
    height: 900px;
    display: flex;
    align-items: center;
    justify-content: center;
    gap: 60px;
  }
  .card {
    width: var(--card-w);
    height: var(--card-h);
    position: relative;
    overflow: hidden;
    box-shadow: 0 10px 28px rgba(0,0,0,0.28);
  }
  .business-name {
    font-family: "Open Sans", Arial, sans-serif;
    font-weight: 700;
    font-size: 30px;
    line-height: 1.15;
    letter-spacing: 0.3px;
    text-align: center;
  }
  .business-name span { display: block; }

  /* Front face */
  .card--front {
    background: var(--black);
    color: var(--paper);
    display: flex;
    align-items: center;
    justify-content: center;
  }

  /* Back face */
  .card--back { background: var(--black); }
  .card__top {
    position: absolute;
    inset: 0 0 auto 0;
    height: 58%;
    background: linear-gradient(180deg, var(--paper-shade), var(--paper) 45%);
    color: var(--black);
    display: flex;
    align-items: center;
    justify-content: center;
  }
  .card__contact {
    position: absolute;
    inset: 58% 0 0 0;
    color: var(--paper);
    font-family: "Open Sans", Arial, sans-serif;
    text-align: center;
    padding-left: 70px;
  }
  .contact__name {
    font-size: 17px;
    font-weight: 600;
    letter-spacing: 0.6px;
    text-transform: uppercase;
    margin-top: 16px;
    margin-bottom: 20px;
  }
  .contact__line {
    font-size: 14px;
    font-weight: 400;
    line-height: 1.45;
  }
</style>
</head>
<body>
  <main class="sheet">
    <section class="card card--front" aria-label="Business card front">
      <h1 class="business-name">
        <span>Briskway Traffic</span>
        <span>Management Plans</span>
      </h1>
    </section>

    <section class="card card--back" aria-label="Business card back">
      <div class="card__top">
        <p class="business-name">
          <span>Briskway Traffic</span>
          <span>Management Plans</span>
        </p>
      </div>
      <div class="card__contact">
        <p class="contact__name">Tom Brindley</p>
        <p class="contact__line">0427 693 058</p>
        <p class="contact__line">harbourlane@zentrynet.com.au</p>
      </div>
    </section>
  </main>
</body>
</html>
```